Business card for Full Stable Works Vanhoorne

I would like to have me designed an professional business card with my existing logo for my company called : full stable works vanhoorne gcv.
I prefer a two sided business card with on the back side only the horses head and the website : fswvanhoorne-example.eu
Only one colour shouldbe all right.
The logo must appear in a nic professional way on the business card.

Other suggestion are welcome.

All copy wrights must be released by the designer after we have selected a final design.

Target Market(s)

Equestrian businesses

Industry/Entity Type

Business

Contact Information for Business Card

Gerard Vanhoorne
Title: zaakvoerder
Full Stable Works Vanhoorne GCV
Lindekouter 47
B - 9999 Voorbeeldegem
België
Phone: + 32 400 98 76 10
Mail: gerard@fswvanhoorne-example.eu

Font styles to use
Serif

Requirements
Must have
• My own logo
• See attached files
• Website: fswvanhoorne-example.eu

```html
<!DOCTYPE html>
<html lang="nl">
<head>
<meta charset="utf-8">
<title>Full Stable Works Vanhoorne – Business Card</title>
<link rel="stylesheet" href="https://fonts.googleapis.com/css2?family=Cinzel:wght@400;700&family=Tinos:wght@700&display=swap">
<style>
  :root {
    --bg: #e9e7e4;
    --card: #ffffff;
    --ink: #2e2e30;
    --ink-soft: #444446;
    --ink-muted: #8f8f92;
    --rule: #6a6a6c;
    --shadow: rgba(0, 0, 0, 0.16);
  }
  * { box-sizing: border-box; margin: 0; padding: 0; }
  html, body {
    width: 1200px; height: 813px; overflow: hidden;
    background: var(--bg);
  }
  .sheet {
    position: relative; width: 1200px; height: 813px;
    display: flex; align-items: center; justify-content: center; gap: 40px;
  }
  .card {
    position: relative; width: 520px; height: 297px;
    background: var(--card);
    box-shadow: 0 6px 20px var(--shadow);
    color: var(--ink);
    font-family: "Cinzel", "Times New Roman", serif;
  }

  /* Front */
  .brand {
    position: absolute; top: 28px; left: 200px; right: 40px;
    display: flex; align-items: center; gap: 12px;
  }
  .brand-dot {
    flex: none; width: 40px; height: 40px; border-radius: 50%;
    background: var(--ink);
  }
  .brand-name {
    font-weight: 700; font-size: 20px; line-height: 1.15; color: var(--ink);
    letter-spacing: 0.5px;
  }
  .rule { position: absolute; height: 1px; background: var(--rule); }
  .rule--top { top: 100px; left: 24px; width: 396px; }
  .rule--bottom { top: 208px; left: 250px; right: 24px; }

  .contact {
    position: absolute; top: 108px; left: 26px; list-style: none;
    font-size: 11.5px; color: var(--ink-soft); letter-spacing: 0.4px;
  }
  .contact li { display: flex; align-items: center; gap: 7px; height: 20px; }
  .contact svg { width: 11px; height: 11px; flex: none; }

  .person { position: absolute; top: 160px; right: 26px; text-align: right; }
  .person-name { font-size: 20px; color: var(--ink-muted); letter-spacing: 0.6px; line-height: 1.1; }
  .person-role { font-size: 15px; color: var(--ink); letter-spacing: 0.8px; line-height: 1.2; }

  .address {
    position: absolute; top: 215px; right: 26px; text-align: right;
    font-style: normal; font-size: 13px; line-height: 1.45; color: var(--ink-soft);
    letter-spacing: 0.6px;
  }

  /* Back */
  .back {
    display: flex; flex-direction: column; align-items: center; justify-content: center; gap: 14px;
  }
  .back-mark { display: flex; align-items: center; gap: 12px; }
  .back-dot { width: 70px; height: 70px; border-radius: 50%; background: var(--ink); }
  .back-name { font-weight: 700; font-size: 16px; line-height: 1.2; color: var(--ink); }
  .website {
    font-family: "Tinos", "Times New Roman", serif; font-weight: 700;
    font-size: 22px; color: var(--ink);
  }
</style>
</head>
<body>
<main class="sheet">
  <section class="card front" aria-label="Voorzijde">
    <div class="brand">
      <span class="brand-dot"></span>
      <span class="brand-name">Full Stable Works Vanhoorne</span>
    </div>
    <div class="rule rule--top"></div>
    <ul class="contact">
      <li>
        <svg viewBox="0 0 12 12" fill="none" stroke="currentColor" stroke-width="1"><rect x="0.5" y="2.5" width="11" height="7"/><path d="M0.5 2.5 L6 7 L11.5 2.5"/></svg>
        + 32 400 98 76 10
      </li>
      <li>
        <svg viewBox="0 0 12 12" fill="none" stroke="currentColor" stroke-width="1"><circle cx="6" cy="6" r="5.5"/><path d="M4 3.5 C3.5 5.5 5.5 8.5 8 8.5 L8.5 7.5 L7.3 6.8 L6.8 7.3 C6 7 5 6 4.8 5.2 L5.3 4.7 L4.7 3.5 Z"/></svg>
        gerard@fswvanhoorne-example.eu
      </li>
    </ul>
    <div class="person">
      <p class="person-name">Gerard Vanhoorne</p>
      <p class="person-role">Zaakvoerder</p>
    </div>
    <div class="rule rule--bottom"></div>
    <address class="address">
      Lindekouter 47<br>
      B - 9999 Voorbeeldegem<br>
      België
    </address>
  </section>

  <section class="card back" aria-label="Achterzijde">
    <div class="back-mark">
      <span class="back-dot"></span>
      <span class="back-name">Full Stable Works<br>Vanhoorne</span>
    </div>
    <p class="website">fswvanhoorne-example.eu</p>
  </section>
</main>
</body>
</html>
```